Skyhaven Robotics Australia, a Sydney based startup need a visiting card designed

We are after a visiting card which is bold and eye catching. We are a drone company providing services and we are also KVR authorized dealer who also sell consumer and industrial drones

Our website is under construction but you can excess from link below.

www.skyhavenrobotics-demo.com.au/test/

Feel free to contact me for any clarifications. we have given 5 days for the project but we are flexible to extend the project to 10 days.

Target Market(s)

Private and government organisation

Industry/Entity Type

Business Service

Contact Information for Business Card

Skyhaven Robotics Australia PTY LTD

Rakesh Menon (Ned) ( Director)

17 Kellow Lane, mirrabell, NSW 2571

Authorized KVR Dealer

0471 382 915 / 1300Skyhavens

info@skyhavenrobotics-demo.com.au

website: www.skyhavenrobotics-demo.com.au

Font styles to use
Serif

Requirements
Must have
• bold and stand out.
Nice to have
• colours complimenting the logo
Should not have
• not black card

```html
<!DOCTYPE html>
<html lang="en">
<head>
<meta charset="utf-8">
<title>Skyhaven Robotics Australia – Business Card</title>
<link href="https://fonts.googleapis.com/css2?family=Roboto:wght@400;500;700;900&display=swap" rel="stylesheet">
<style>
  :root {
    --navy: #0d2d4a;
    --navy-deep: #0a2540;
    --gold: #f5b21b;
    --ink: #2b2f36;
    --paper: #ffffff;
    --stage: #e9ebee;
    --teal-a: #1f5b78;
    --teal-b: #2f6e72;
  }
  * { box-sizing: border-box; margin: 0; padding: 0; }
  html, body { width: 1200px; height: 900px; overflow: hidden; }
  body {
    background: var(--stage);
    font-family: "Roboto", Arial, sans-serif;
    position: relative;
  }
  .card {
    position: absolute;
    left: 250px;
    width: 700px;
    height: 400px;
    border-radius: 22px;
    overflow: hidden;
    box-shadow: 0 10px 30px rgba(0,0,0,.18);
  }
  /* Front */
  .card-front { top: 40px; background: var(--paper); }
  .card-front .wave { position: absolute; inset: 0; width: 100%; height: 100%; }
  .brand-front {
    position: absolute; left: 40px; top: 70px; width: 250px;
    display: flex; align-items: center; gap: 14px;
  }
  .brand-dot { width: 46px; height: 46px; border-radius: 50%; background: var(--gold); flex: none; }
  .brand-name {
    font-weight: 900; font-size: 28px; line-height: 1.05; color: var(--navy);
    text-transform: uppercase; letter-spacing: .5px;
  }
  .divider {
    position: absolute; left: 318px; top: 60px; width: 2px; height: 190px;
    background: var(--gold);
  }
  .contact { position: absolute; left: 345px; top: 70px; color: var(--ink); }
  .contact .person { font-weight: 900; font-size: 27px; color: var(--navy); letter-spacing: .5px; }
  .contact .role { font-size: 16px; margin-top: 2px; }
  .contact .address { font-size: 16px; line-height: 1.3; margin-top: 10px; }
  .contact ul { list-style: none; margin-top: 6px; }
  .contact li { font-size: 16px; line-height: 1.45; display: flex; align-items: center; gap: 10px; }
  .contact li svg { width: 13px; height: 13px; flex: none; fill: var(--navy); }
  .accent { color: var(--gold); }
  /* Back */
  .card-back { top: 470px; }
  .backdrop {
    position: absolute; inset: 0;
    background: linear-gradient(120deg, var(--teal-b) 0%, var(--teal-a) 55%, #174a66 100%);
  }
  .brand-back {
    position: absolute; left: 0; right: 0; top: 130px;
    display: flex; justify-content: center; align-items: center; gap: 16px;
  }
  .brand-back .brand-name { color: var(--paper); font-size: 34px; }
  .web-back {
    position: absolute; left: 0; right: 0; top: 270px; text-align: center;
    color: var(--paper); font-size: 20px; font-weight: 500;
  }
</style>
</head>
<body>

<section class="card card-front">
  <svg class="wave" viewBox="0 0 700 400" preserveAspectRatio="none" aria-hidden="true">
    <path d="M0 255 C180 300 420 300 545 335 C610 352 640 380 660 400 L0 400 Z" fill="#0d2d4a"/>
    <path d="M0 250 C180 295 420 292 545 325 C615 345 645 375 668 400 L660 400 C640 380 610 352 545 335 C420 300 180 300 0 262 Z" fill="#f5b21b"/>
    <path d="M0 262 C180 300 420 300 545 335 C610 352 640 380 660 400 L652 400 C630 384 600 360 540 343 C420 310 180 310 0 272 Z" fill="#ffffff"/>
  </svg>

  <div class="brand-front">
    <span class="brand-dot"></span>
    <span class="brand-name">Skyhaven Robotics Australia</span>
  </div>

  <div class="divider"></div>

  <div class="contact">
    <h1 class="person">DARREN HOLT</h1>
    <p class="role">Managing Director</p>
    <p class="address">4820 Harbour Crescent,<br>Westvale, Qc J2K 3L4</p>
    <ul>
      <li><svg viewBox="0 0 16 16"><rect x="4" y="1" width="8" height="14" rx="1.5"/></svg>555-203-4417</li>
      <li><svg viewBox="0 0 16 16"><path d="M3 1l3 3-2 2c1 2 3 4 5 5l2-2 3 3-2 2C7 14 2 9 1 3z"/></svg>555-203-4418</li>
      <li><svg viewBox="0 0 16 16"><path d="M1 3h14v10H1z M2 4l6 5 6-5" fill="none" stroke="#0d2d4a" stroke-width="1.5"/></svg>darren@skyhavenrobotics-demo.com.au</li>
      <li><svg viewBox="0 0 16 16"><circle cx="8" cy="8" r="7"/></svg>www.<span class="accent">skyhavenrobotics-demo</span>.com.au</li>
    </ul>
  </div>
</section>

<section class="card card-back">
  <div class="backdrop" role="img" aria-label="Photo of a branded service vehicle and equipment trailer on a grassy field, tinted blue"></div>
  <div class="brand-back">
    <span class="brand-dot"></span>
    <span class="brand-name">Skyhaven Robotics Australia</span>
  </div>
  <p class="web-back">www.<span class="accent">skyhavenrobotics-demo</span>.com.au</p>
</section>

</body>
</html>
```